Brevant Business Card

I have a business that is called "Brevant Electrical Products LTD" My company deals with top of the range laptops and mobile phones that are exclusive. I need a business card that will be eye catching but not over complicated.

Target Market(s)

Adults aged 19 to 50
Upper middle class

Industry/Entity Type

Business

Requirements
Must have
• Company name/logo (file attached)
• It must have my contact information which is:

• Name: Dale Marwick

• Position: Managing Director 

• Business Address: 7 Hapton Row, London, W4 9QD

• Contact Number: 02085193604
• Mobile: 07814260537
• Email: info@brevant-goods.co.uk
Nice to have
• Simple and stylish
• Eye catching

```html
<!DOCTYPE html>
<html lang="en">
<head>
<meta charset="utf-8">
<title>Brevant Electrical Products – Business Card</title>
<link rel="stylesheet" href="https://fonts.googleapis.com/css2?family=Questrial&family=Arimo:wght@400;700&display=swap">
<style>
  :root {
    --page-bg: #eaf3f8;
    --card-bg: #ffffff;
    --brand-blue: #2aade0;
    --tagline-blue: #2a8fb8;
    --band-teal: #1e9fc6;
    --wash-light: #d7eef6;
    --wash-mid: #9fd7ea;
    --ink: #111111;
    --card-shadow: 3px 4px 6px rgba(0, 0, 0, 0.45);
  }
  * { margin: 0; padding: 0; box-sizing: border-box; }
  html, body {
    width: 1200px;
    height: 1143px;
    overflow: hidden;
    background: var(--page-bg);
  }
  .canvas {
    position: relative;
    width: 1200px;
    height: 1143px;
  }
  .card {
    position: absolute;
    background: var(--card-bg);
    box-shadow: var(--card-shadow);
    overflow: hidden;
  }

  .brand-name {
    font-family: "Questrial", sans-serif;
    color: var(--brand-blue);
    line-height: 1;
    text-transform: uppercase;
    white-space: nowrap;
  }
  .brand-tagline {
    font-family: "Questrial", sans-serif;
    color: var(--tagline-blue);
    line-height: 1;
    letter-spacing: 0.5px;
    white-space: nowrap;
  }

  /* Front of card */
  .card-front {
    left: 127px;
    top: 141px;
    width: 514px;
    height: 281px;
  }
  .card-front .wash {
    position: absolute;
    left: 0;
    top: 0;
    width: 280px;
    height: 281px;
    background: linear-gradient(90deg, var(--wash-mid) 0%, var(--wash-light) 55%, rgba(255,255,255,0) 100%);
  }
  .card-front .brand {
    position: absolute;
    left: 22px;
    top: 80px;
  }
  .card-front .brand-name { font-size: 50px; letter-spacing: 1px; }
  .card-front .brand-tagline { font-size: 19px; margin: 8px 0 0 28px; }

  .holder {
    position: absolute;
    right: 20px;
    top: 26px;
    text-align: right;
    font-family: "Arimo", sans-serif;
    color: var(--ink);
  }
  .holder-name { font-size: 17px; font-weight: 700; }
  .holder-role { font-size: 14px; margin-top: 3px; }

  .contact {
    position: absolute;
    right: 20px;
    top: 188px;
    text-align: right;
    font-family: "Arimo", sans-serif;
    font-style: normal;
    font-size: 14px;
    line-height: 19px;
    color: var(--ink);
  }

  /* Back of card */
  .card-back {
    left: 559px;
    top: 434px;
    width: 487px;
    height: 285px;
  }
  .card-back .wash {
    position: absolute;
    left: 0;
    top: 0;
    width: 390px;
    height: 285px;
    background: radial-gradient(ellipse at 30% 45%, var(--wash-light) 0%, var(--wash-mid) 40%, rgba(255,255,255,0.2) 75%, rgba(255,255,255,0) 100%);
  }
  .card-back .brand {
    position: absolute;
    left: 50px;
    top: 92px;
    width: 372px;
    text-align: center;
  }
  .card-back .brand-name { font-size: 74px; letter-spacing: 1px; }
  .card-back .brand-tagline { font-size: 31px; margin-top: 10px; }

  .web-band {
    position: absolute;
    right: 10px;
    top: 8px;
    width: 40px;
    height: 269px;
    background: var(--band-teal);
    display: flex;
    align-items: center;
    justify-content: center;
  }
  .web-address {
    writing-mode: vertical-rl;
    font-family: "Arimo", sans-serif;
    font-weight: 700;
    font-size: 15px;
    color: var(--ink);
  }

  /* Standalone logotype */
  .logotype {
    position: absolute;
    left: 0;
    width: 1200px;
    top: 808px;
    text-align: center;
  }
  .logotype .brand-name { font-size: 112px; letter-spacing: 4px; }
  .logotype .brand-tagline { font-size: 50px; margin-top: 18px; letter-spacing: 1.5px; }
</style>
</head>
<body>
<main class="canvas">

  <section class="card card-front" aria-label="Business card front">
    <div class="wash" role="img" aria-label="Soft blue brand backdrop"></div>
    <div class="brand">
      <div class="brand-name">Brevant</div>
      <div class="brand-tagline">Electrical Products</div>
    </div>
    <div class="holder">
      <p class="holder-name">Dale Marwick</p>
      <p class="holder-role">Managing Director</p>
    </div>
    <address class="contact">
      7 Hapton Row<br>
      London, W4 9QD<br>
      t. 02085193604 m. 07814260537<br>
      info@brevant-goods.co.uk
    </address>
  </section>

  <section class="card card-back" aria-label="Business card back">
    <div class="wash" role="img" aria-label="Soft blue brand backdrop"></div>
    <div class="brand">
      <div class="brand-name">Brevant</div>
      <div class="brand-tagline">Electrical Products</div>
    </div>
    <div class="web-band">
      <span class="web-address">www.brevant-goods.co.uk</span>
    </div>
  </section>

  <section class="logotype" aria-label="Company name">
    <div class="brand-name">Brevant</div>
    <div class="brand-tagline">Electrical Products</div>
  </section>

</main>
</body>
</html>
```